Flyer-Design für Kreativwerkstatt
Zielgruppe
Kreativwerkstatt für Touristen - vorrangig Frauen
Aufgabenstellung
1 mal gefaltet
Wenn möglich außer dem Logo noch folgenden Text verwenden
Kreativität fängt da ,wo der Verstand aufhört das denken zu behindern

```html
<!DOCTYPE html>
<html lang="de">
<head>
<meta charset="utf-8">
<title>Bastelhof – Flyer Kreativwerkstatt</title>
<link rel="stylesheet" href="https://fonts.googleapis.com/css2?family=Jost:wght@400;500&display=swap">
<style>
  :root {
    --backdrop: #ece6da;
    --paper: #f6eecb;
    --paper-light: #f8f1d6;
    --fold: #e2d6aa;
    --cutout: #6a4a36;
    --ink: #6e2a17;
    --accent: #e0821e;
    --accent-deep: #cc5a10;
    --faint-art: #f1dcaa;
  }
  * { margin: 0; padding: 0; box-sizing: border-box; }
  html, body { width: 1200px; height: 864px; overflow: hidden; }
  body {
    background: var(--backdrop);
    font-family: "Jost", "Futura", sans-serif;
    color: var(--ink);
    position: relative;
  }
  .flyer {
    position: absolute;
    left: 150px; top: 102px;
    width: 900px; height: 660px;
    display: flex;
    box-shadow: 0 10px 30px rgba(60, 40, 20, 0.25);
  }
  .panel {
    position: relative;
    width: 450px; height: 660px;
    background: var(--paper);
    overflow: hidden;
  }
  .panel--inside-left { border-right: 1px solid var(--fold); }
  .panel--inside-right { background: var(--paper-light); }

  .cutout {
    position: absolute;
    left: 48px; top: 44px;
    width: 352px; height: 180px;
    border-radius: 50%;
    background: radial-gradient(ellipse at 70% 70%, #84624a, var(--cutout) 60%, #4f3528);
  }
  .intro {
    position: absolute;
    left: 48px; top: 270px; width: 360px;
    font-size: 17px; line-height: 1.25;
  }
  .backdrop-art {
    position: absolute;
    left: 0; bottom: 0;
    width: 450px; height: 230px;
    background: linear-gradient(180deg, rgba(241,220,170,0) 0%, var(--faint-art) 55%, rgba(241,220,170,0.6) 100%);
  }

  .brand {
    position: absolute;
    left: 42px; top: 44px;
    width: 330px; height: 150px;
    display: flex; align-items: center; justify-content: center;
    gap: 12px;
  }
  .brand__dot {
    width: 14px; height: 14px; border-radius: 50%;
    background: var(--accent);
  }
  .brand__name {
    font-size: 46px; font-weight: 500;
    color: var(--accent);
  }
  .benefits {
    position: absolute;
    left: 42px; top: 230px; width: 340px;
    list-style: none;
    font-size: 16.5px; line-height: 1.2;
  }
  .benefits li {
    position: relative;
    padding-left: 18px;
    margin-bottom: 20px;
  }
  .benefits li::before {
    content: "";
    position: absolute; left: 0; top: 9px;
    width: 5px; height: 5px; border-radius: 50%;
    background: var(--ink);
  }
  .summary {
    position: absolute;
    left: 42px; top: 440px; width: 360px;
    font-size: 19px; line-height: 1.2;
  }
  .cta {
    position: absolute;
    left: 42px; top: 560px;
    width: 408px; height: 70px;
    background: linear-gradient(90deg, var(--accent) 0%, var(--accent-deep) 100%);
    color: #fbe9c8;
    font-size: 20px; font-weight: 500; line-height: 1.2;
    display: flex; align-items: center; justify-content: center;
    text-align: center;
  }
</style>
</head>
<body>
  <main class="flyer">
    <section class="panel panel--inside-left">
      <div class="cutout" aria-hidden="true"></div>
      <p class="intro">Wir möchten Sie mit traditionellen Handwerk und modernen Materialen, das traditionale Handwerk, mit und um das Papier vertraut machen. Dies kann durch verschiedene Kurse von Ihnen genutzt werden.</p>
      <div class="backdrop-art" role="img" aria-label="Blasse Illustration: Baumkronen über einem aufgeschlagenen Buch als Dach"></div>
    </section>

    <section class="panel panel--inside-right">
      <div class="brand">
        <span class="brand__dot" aria-hidden="true"></span>
        <span class="brand__name">Bastelhof</span>
      </div>
      <ul class="benefits">
        <li>Sie können Ihr eignes besonderes Papier herstellen</li>
        <li>Sie schaffen einen würdigen "Schuhkarton" für ihre Schätze</li>
        <li>Sie gestalten Ihr eigenes Buch</li>
        <li>Sie lernen wie Sie durch Leder ihr Buch in Szene setzen</li>
      </ul>
      <p class="summary">Dies und noch viele Anregungen und Möglichkeiten können Sie in Schnupperkurs, Einsteigerkurs oder Fortgeschrittenen Kurs erleben.</p>
      <div class="cta">Jetzt anmelden und eine<br>besondere Auszeit genießen!</div>
    </section>
  </main>
</body>
</html>
```